Gratefl Moments/Coral Friday

Create a double sided postcard which will be distributed to 60,000 destinations, suitable for printing on re-cycled card.

Promotional offer ends Sunday August 31st 2014

It is Winter in Perth Western Australia, colours need to be bright and a reminder of summer. The card needs to be fun with a Mediterranean Spanish type feel
web site www.kelvport.com.au

```html
<!DOCTYPE html>
<html lang="en">
<head>
<meta charset="utf-8">
<title>Kelvport – Lunch Offer</title>
<link rel="stylesheet" href="https://fonts.googleapis.com/css2?family=EB+Garamond:wght@400;600;700&display=swap">
<style>
  :root {
    --stage: #6a6b6e;
    --paper: #ffffff;
    --ink: #5b5b5d;
    --rose: #d68cb1;
    --ocean: #1470b0;
    --logo-blue: #1d6fb0;
    --salmon: #ef8a66;
    --wood: #c9a47a;
    --slate: #4a4a48;
  }
  * { box-sizing: border-box; margin: 0; padding: 0; }
  html, body { width: 910px; height: 1200px; overflow: hidden; }
  body {
    background: var(--stage);
    font-family: "EB Garamond", Georgia, serif;
    position: relative;
  }
  .postcard {
    position: absolute;
    left: 101px; top: 107px;
    width: 700px; height: 985px;
    background: var(--paper);
    overflow: hidden;
  }
  .headline {
    position: absolute;
    left: 54px; top: 72px;
    color: var(--ink);
    font-size: 44px;
    line-height: 53px;
    font-weight: 400;
  }
  .headline strong { font-weight: 700; }
  .hero-photo {
    position: absolute;
    left: 0; top: 288px;
    width: 700px; height: 327px;
    background:
      linear-gradient(168deg, transparent 0 44%, var(--salmon) 44% 74%, transparent 74%),
      linear-gradient(180deg, var(--slate) 0 40%, var(--wood) 40% 100%);
  }
  .price-badge {
    position: absolute;
    left: 486px; top: 224px;
    width: 164px; height: 164px;
    border-radius: 50%;
    background: var(--rose);
    border: 5px solid var(--paper);
    color: var(--paper);
    text-align: center;
    font-weight: 700;
    padding-top: 38px;
  }
  .price-badge .amount { display: block; font-size: 37px; line-height: 38px; }
  .price-badge .unit { display: block; font-size: 19px; line-height: 20px; }
  .hours-band {
    position: absolute;
    left: 0; top: 615px;
    width: 700px; height: 44px;
    background: var(--rose);
    color: var(--paper);
    font-weight: 700;
    font-size: 20px;
    line-height: 44px;
    text-align: right;
    padding-right: 10px;
  }
  .offer-band {
    position: absolute;
    left: 0; top: 659px;
    width: 700px; height: 186px;
    background: var(--ocean);
    color: var(--paper);
    text-align: right;
    padding: 40px 60px 0 0;
    font-size: 20px;
    line-height: 28px;
  }
  .offer-band strong { font-weight: 700; }
  .web-address {
    position: absolute;
    left: 62px; top: 910px;
    color: var(--ink);
    font-weight: 700;
    font-size: 15px;
  }
  .brand-name {
    position: absolute;
    left: 405px; top: 893px;
    color: var(--logo-blue);
    font-weight: 600;
    font-size: 32px;
    letter-spacing: 3px;
  }
</style>
</head>
<body>
  <article class="postcard">
    <h1 class="headline">Gratefl Moments with<br>Lunch overlooking <strong>Perth’s<br>most beautiful Bay</strong></h1>

    <div class="hero-photo" role="img" aria-label="Photo of sliced salmon on a wooden board with a dish of soy sauce and chopsticks"></div>

    <div class="price-badge">
      <span class="amount">$48.00</span>
      <span class="unit">per person</span>
    </div>

    <p class="hours-band">(Available Monday to Friday 11am until 3pm)</p>

    <p class="offer-band">
      Select one dish from each course with<br>
      your choice of either a glass of<br>
      <strong>Bellavento Soave 2011 or<br>
      Santa Lucea ValpolicellaClassico 2011</strong>
    </p>

    <p class="web-address">www.kelvport.com.au</p>
    <p class="brand-name">KELVPORT</p>
  </article>
</body>
</html>
```